Business Card Design

Hoping for a black background business card, minimalistic design.
With the Copper Lantern logo you created in white.

I would like to include:
My Name and title
Address (street address)
Reception: (phone number)
Fax: (fax number)
Reception: (email address)
Direct email: (email address)
Instagram: (ig handle)

```html
<!DOCTYPE html>
<html lang="en">
<head>
<meta charset="utf-8">
<title>Copper Lantern – Business Card</title>
<link href="https://fonts.googleapis.com/css2?family=Montserrat:wght@400;500;600&display=swap" rel="stylesheet">
<style>
  :root {
    --backdrop: #cccccc;
    --card: #000000;
    --ring: #333333;
    --ink: #ffffff;
  }
  * { margin: 0; padding: 0; box-sizing: border-box; }
  html, body { width: 1000px; height: 1200px; overflow: hidden; }
  body {
    background: var(--backdrop);
    font-family: "Montserrat", Arial, sans-serif;
    color: var(--ink);
    position: relative;
  }
  .card {
    position: absolute;
    left: 50px;
    width: 899px;
    height: 540px;
    background: var(--card);
    overflow: hidden;
  }
  .card--back { top: 43px; }
  .card--front { top: 617px; }
  .card__ring {
    position: absolute;
    left: 0; top: 0;
    width: 100%; height: 100%;
  }
  .contact {
    position: absolute;
    left: 507px;
    top: 108px;
  }
  .contact__name {
    font-size: 28px;
    font-weight: 600;
    line-height: 38px;
  }
  .contact__title {
    font-size: 28px;
    font-weight: 400;
    line-height: 36px;
    margin-bottom: 12px;
  }
  .contact__list { list-style: none; }
  .contact__item {
    display: flex;
    align-items: center;
    height: 44px;
    font-size: 25px;
    font-weight: 400;
    letter-spacing: 0.3px;
  }
  .contact__icon {
    width: 26px; height: 26px;
    margin-right: 12px;
    flex: none;
  }
  .brand {
    position: absolute;
    left: 0; top: 0;
    width: 100%; height: 100%;
  }
  .brand__name {
    position: absolute;
    left: 341px;
    top: 246px;
    font-size: 37px;
    font-weight: 500;
    letter-spacing: 2px;
    text-transform: uppercase;
    line-height: 46px;
    white-space: nowrap;
  }
</style>
</head>
<body>

<section class="card card--back">
  <svg class="card__ring" viewBox="0 0 899 540" aria-hidden="true">
    <circle cx="284" cy="270" r="278" fill="none" stroke="var(--ring)" stroke-width="30"/>
  </svg>

  <div class="contact">
    <p class="contact__name">Your Name</p>
    <p class="contact__title">Manager</p>
    <ul class="contact__list">
      <li class="contact__item">
        <svg class="contact__icon" viewBox="0 0 26 26" aria-hidden="true">
          <rect width="26" height="26" rx="3" fill="#fff"/>
          <path d="M8 6c1-1 2 0 3 2s0 2-1 3c1 2 3 4 5 5 1-1 1-2 3-1s3 2 2 3c-1 2-3 2-5 1-4-2-7-5-8-9-1-2 0-3 1-4z" fill="#000"/>
        </svg>123 444 555
      </li>
      <li class="contact__item">
        <svg class="contact__icon" viewBox="0 0 26 26" aria-hidden="true">
          <rect width="26" height="26" rx="3" fill="#fff"/>
          <path d="M13 4a6 6 0 0 0-6 6c0 4 6 10 6 10s6-6 6-10a6 6 0 0 0-6-6z" fill="none" stroke="#000" stroke-width="2"/>
          <circle cx="13" cy="10" r="2" fill="#000"/>
          <line x1="8" y1="22" x2="18" y2="22" stroke="#000" stroke-width="2"/>
        </svg>789 Your Street Here
      </li>
      <li class="contact__item">
        <svg class="contact__icon" viewBox="0 0 26 26" aria-hidden="true">
          <rect width="26" height="26" rx="3" fill="#fff"/>
          <rect x="5" y="7.5" width="16" height="11" fill="none" stroke="#000" stroke-width="1.6"/>
          <path d="M5 7.5l8 6 8-6M5 18.5l6-5M21 18.5l-6-5" fill="none" stroke="#000" stroke-width="1.4"/>
        </svg>info@yourname.com
      </li>
      <li class="contact__item">
        <svg class="contact__icon" viewBox="0 0 26 26" aria-hidden="true">
          <rect width="26" height="26" rx="3" fill="#fff"/>
          <circle cx="13" cy="13" r="7.5" fill="none" stroke="#000" stroke-width="1.5"/>
          <ellipse cx="13" cy="13" rx="3.2" ry="7.5" fill="none" stroke="#000" stroke-width="1.3"/>
          <path d="M5.5 13h15M7 9h12M7 17h12" stroke="#000" stroke-width="1.2"/>
        </svg>www.yourname.com
      </li>
      <li class="contact__item">
        <svg class="contact__icon" viewBox="0 0 26 26" aria-hidden="true">
          <rect width="26" height="26" rx="3" fill="#fff"/>
          <rect x="6" y="6" width="14" height="14" fill="none" stroke="#000" stroke-width="1.8"/>
        </svg>www.yourname.com
      </li>
    </ul>
  </div>
</section>

<section class="card card--front">
  <svg class="card__ring" viewBox="0 0 899 540" aria-hidden="true">
    <circle cx="656" cy="280" r="278" fill="none" stroke="var(--ring)" stroke-width="30"/>
  </svg>
  <svg class="brand" viewBox="0 0 899 540" aria-hidden="true">
    <circle cx="241" cy="268" r="60" fill="none" stroke="var(--ink)" stroke-width="6"/>
    <line x1="323" y1="206" x2="323" y2="332" stroke="var(--ink)" stroke-width="2"/>
  </svg>
  <p class="brand__name">Copper Lantern</p>
</section>

</body>
</html>
```